blaze otto: flyer/menu board design for modern food van/trailer concept.

who are we? a modern food van/trailer selling restuarant quality food (burrito, burgers, waffles).our demographic is 16 - 35.

what do we need? a design for a flyer A4 size that is divided in 3 sections.with our menu on the inside and a design on the outside with our logo. the style must be funky, cool and modern.

Our restaurant theme is based on the movie "stone moth" by lorcan vedrassi. So any designs should be somehow linked to that genre.

the same menu on the flyer will be posted on our menu board. there is a chance we will use an lcd menu board so the format must accomodate that.
the menu must also be easilly modified in case we need to update changes pricing and menu items.

thank you
team blaze otto
Updates

Hi, Project will become non-refundable as soon as i get some good designs. Thank you and good luck Team blaze otto

Dear designers, I have uploaded some example menus, pics, my logo and hand drawings of my vision of how i would like the flyer/menu to look like. I understand that some designers cant see my uploads. I have contacted pixel harbor and they are trying to fix the issue. The deadline will be extended if needed. Thank you for your patients and your designs. Regards, Otto

Hi, To those who are having trouble viewing my uploads, here is the link http://gigs.pixelharbrio.com/job.aspx?id=519370

Target Market(s)

our target market is young and cool between the ages of16 - 35. we are a multicultural society in a western governed country. Sydney Australia.

Industry/Entity Type

Restaurant

Font styles to use
Serif

Requirements
Must have
• pictures of menu items in a hand drawn black and white style: burger, burrito, waffles, buffallo wings, chicken, beef, prawn. examples provided
please feel free to show off your alternate ideas.
style should be modern, cool and funky. examples provided
Nice to have
• Colours: yellow, red, black.
Pictures/illustrations: black & white in a sketch style.
Theme: ninja, Mexican, modern, funky.

```html
<!DOCTYPE html>
<html lang="en">
<head>
<meta charset="utf-8">
<title>Otto's Grill – Inside Menu</title>
<link rel="stylesheet" href="https://fonts.googleapis.com/css2?family=Bangers&family=Architects+Daughter&display=swap">
<style>
  :root{
    --bg:#3a2416;
    --yellow:#f4cd22;
    --yellow-light:#f8dc4a;
    --orange:#e4801a;
    --red:#b0201a;
    --ink:#161310;
    --paper:#f7f1dc;
    --paper-edge:#d9661a;
  }
  *{box-sizing:border-box;margin:0;padding:0}
  html,body{width:1200px;height:1000px;overflow:hidden;background:var(--bg)}
  .menu{
    position:absolute;left:30px;top:60px;width:1140px;height:880px;
    display:grid;grid-template-columns:repeat(3,1fr);
    background:radial-gradient(ellipse at 50% 45%, var(--yellow-light) 0%, var(--yellow) 45%, var(--orange) 88%, var(--paper-edge) 100%);
    color:var(--ink);
    font-family:"Architects Daughter", cursive;
    box-shadow:0 10px 30px rgba(0,0,0,.45);
    overflow:hidden;
  }
  .panel{position:relative;padding:22px 26px 20px;display:flex;flex-direction:column;min-width:0}
  .panel + .panel{border-left:1px solid rgba(120,60,10,.25)}
  .brand{font-family:"Architects Daughter", cursive;font-weight:400;font-size:38px;line-height:1;color:var(--ink)}
  .section-head{display:flex;justify-content:space-between;align-items:flex-start;gap:10px;margin-top:6px}
  .section-title{font-family:"Bangers", cursive;font-weight:400;color:var(--red);font-size:36px;line-height:1;letter-spacing:1px}
  .tagline{font-size:14px;line-height:1.25;text-transform:uppercase;font-weight:400}
  .price{font-family:"Bangers", cursive;font-size:36px;line-height:1;white-space:nowrap}
  .price sup{font-size:17px;vertical-align:top;margin-left:2px}
  .art{background:linear-gradient(135deg,#f5e7b0,#c9b37a);border:2px solid var(--ink);border-radius:8px;opacity:.85;flex:none}
  .bar{
    background:var(--ink);color:var(--yellow);
    font-family:"Bangers", cursive;font-size:22px;letter-spacing:1px;line-height:1.2;
    padding:3px 16px;margin:12px -26px 8px;transform:rotate(1.5deg);text-transform:uppercase;
  }
  .bar small{font-size:16px;color:var(--yellow-light)}
  .items{list-style:none;font-size:12.5px;line-height:1.3;text-transform:uppercase}
  .items li{position:relative;padding-left:18px;margin-bottom:4px}
  .items li::before{
    content:"";position:absolute;left:0;top:2px;width:11px;height:11px;background:var(--ink);
    clip-path:polygon(50% 0,62% 38%,100% 50%,62% 62%,50% 100%,38% 62%,0 50%,38% 38%);
  }
  .items b{color:var(--red);font-weight:400}
  .sauces{display:grid;grid-template-columns:1fr 1fr;gap:2px 10px}
  .sauces .level{color:var(--red)}
  .extras{font-size:12.5px;text-transform:uppercase;margin-top:8px;display:flex;gap:4px 14px;flex-wrap:wrap}
  .extras span{color:var(--red)}
  .meal{margin-top:auto;display:flex;align-items:flex-end;gap:12px}
  .meal-text{font-size:13px;text-transform:uppercase}
  .ribbon{
    display:inline-block;background:#f7e9b5;border:2px solid var(--ink);white-space:nowrap;
    font-family:"Bangers", cursive;font-size:17px;letter-spacing:1px;padding:2px 18px;margin-bottom:10px;
    clip-path:polygon(0 0,100% 0,94% 50%,100% 100%,0 100%,6% 50%);
  }
  .notepad{background:var(--paper);border:1px solid #9a8a60;padding:8px 12px;width:180px;transform:rotate(-2deg);flex:none}
  .notepad h3{font-family:"Bangers", cursive;font-weight:400;font-size:17px;letter-spacing:1px;border-bottom:2px solid var(--red)}
  .notepad li{list-style:none;font-size:13px;display:flex;justify-content:space-between;border-bottom:1px solid #c9bfa0;padding:2px 0;white-space:nowrap;text-transform:uppercase}
  .notepad li span{color:var(--red)}
  .price-list li{display:flex;justify-content:space-between;gap:8px}
  .price-list .amt{font-family:"Bangers", cursive;font-size:18px;white-space:nowrap;letter-spacing:1px}
  .blurb{font-size:13px;text-transform:uppercase;line-height:1.35}
  .fineprint{font-size:9.5px;text-transform:uppercase;line-height:1.3;margin-top:auto}
</style>
</head>
<body>
<main class="menu">
  <section class="panel panel-burritos">
    <h1 class="brand">Otto's Grill</h1>
    <div class="section-head">
      <div>
        <h2 class="section-title">Burritos</h2>
        <p class="tagline">Whats a burrito?<br>&nbsp;&nbsp;A Mexican kebab mate!</p>
      </div>
      <div style="text-align:right">
        <div class="art" role="img" aria-label="Sketch of two wrapped burritos" style="width:100px;height:44px;margin-bottom:4px"></div>
        <div class="price">$9<sup>.00</sup></div>
      </div>
    </div>
    <div class="bar">Step 1: Choose your style</div>
    <ul class="items">
      <li><b>Original:</b> lettuce, salsa, guacamole &amp; sour cream.</li>
      <li><b>Fuego:</b> grilled capsicum &amp; onion, salsa, guacamole &amp; sour cream.</li>
      <li><b>California:</b> fries, cheese, salsa, guacamole &amp; sour cream.</li>
    </ul>
    <div class="bar">Step 2: Choose your filling</div>
    <ul class="items">
      <li><b>Mexican chicken:</b> marinated fillet.</li>
      <li><b>Chipotle steak:</b> juicy char grilled steak.</li>
      <li><b>Fish fillet:</b> flash fried.</li>
      <li><b>Saute prawn:</b> with lemon &amp; herb.</li>
    </ul>
    <div class="bar">Step 3: Add a sauce <small>(optional)</small></div>
    <ul class="items sauces">
      <li>Corriander &amp; lime <span class="level">(mild)</span></li>
      <li>Chipotle <span class="level">(medium)</span></li>
      <li>Hot sauce <span class="level">(hot)</span></li>
      <li>Habannero <span class="level">(insane)</span></li>
    </ul>
    <p class="extras"><span>Extras</span> $1.00 <span>Guacamole</span> $2.00 <span>Extra filling</span> $3.00</p>
    <div class="meal">
      <div>
        <div class="ribbon">Make it a meal</div>
        <p class="meal-text">Fries, sauce<br>and drink</p>
      </div>
      <div class="art" role="img" aria-label="Sketch of fries, a drink and a sauce pot" style="width:100px;height:70px"></div>
      <div class="price">$4<sup>.50</sup></div>
    </div>
  </section>

  <section class="panel panel-burgers">
    <div class="section-head" style="margin-top:34px">
      <div>
        <h2 class="section-title">Burgers</h2>
        <p class="tagline">Out of this world!</p>
      </div>
      <div class="art" role="img" aria-label="Sketch of a stacked burger" style="width:100px;height:60px"></div>
      <div class="price" style="align-self:flex-end">$9<sup>.00</sup></div>
    </div>
    <div class="bar">Beef: <small>200 gram! You got beef wid dat?</small></div>
    <ul class="items">
      <li><b>Classic beef:</b> lettuce, tomato, grilled onion, BBQ sauce.</li>
      <li><b>Aussie burger:</b> lettuce, tomato, grilled onion, pineapple, beef rashes, BBQ sauce.</li>
      <li><b>American:</b> coleslaw, tomatoe, fries, pickles, mayo, ketchup.</li>
      <li><b>Cheese burger:</b> cheese, pickles, onion, mustard, ketchup, mayo.</li>
      <li><b>Backyard burger:</b> lettuce, tomato, cheese, pickles, onion, mustard, ketchup, mayo.</li>
      <li><b>Surf n turf:</b> lettuce, tomatoe, calamari, harrissa paste, ketchup, mayo.</li>
    </ul>
    <div class="bar">Chicken: <small>mmm chiiigen...</small></div>
    <ul class="items">
      <li><b>Classic chicken:</b> lettuce, mayo.</li>
      <li><b>Krispy:</b> crispy chicken tenders, lettuce, cheese, feisty mayo.</li>
      <li><b>Chicken n chips:</b> crispy chicken tenders, fries, coleslaw, cheese, feisty mayo.</li>
      <li><b>Mexican:</b> grilled chicken breast, lettuce, salsa, guacamole, southwest sauce.</li>
      <li><b>Portuguese:</b> grilled chicken breast, lettuce, cheese, mayo, perri perri.</li>
      <li><b>Lebanese:</b> grilled chicken breast, fries, Lebanese pickles, garlic sauce.</li>
    </ul>
    <p class="extras"><span>Extras</span> $1.00 <span>Double beef or chicken</span> $4.50 <span>Guacamole</span> $2.00</p>
    <div class="meal">
      <div>
        <div class="ribbon">Make it a meal</div>
        <p class="meal-text">Fries, sauce<br>and drink</p>
      </div>
      <div class="art" role="img" aria-label="Sketch of fries, a drink and a sauce pot" style="width:100px;height:70px"></div>
      <div class="price">$4<sup>.50</sup></div>
    </div>
  </section>

  <section class="panel panel-sides">
    <div class="section-head" style="margin-top:34px;align-items:center">
      <h2 class="section-title" style="font-size:28px">Buffalo Chicken Ribs</h2>
      <div class="art" role="img" aria-label="Sketch of chicken wings" style="width:60px;height:40px"></div>
    </div>
    <p class="tagline">Is when a buffalo makes<br>&nbsp;&nbsp;&nbsp;&nbsp;love to a chicken...<br>Drenched in sauce &amp; served with ranch.</p>
    <div style="display:flex;gap:14px;margin-top:12px;align-items:flex-start">
      <div class="notepad">
        <h3>Death list pack</h3>
        <ul>
          <li>1. 6 pack: <span>$4.95</span></li>
          <li>2. 12 pack: <span>$7.95</span></li>
          <li>3. 24 pack: <span>$14.95</span></li>
        </ul>
      </div>
      <div style="min-width:0">
        <ul class="items"><li><b>Sauces:</b><br>Lemon &amp; herb, BBQ, hot sauce, perri perri.</li></ul>
        <div class="art" role="img" aria-label="Sketch of a katana sword" style="width:120px;height:20px;margin-top:10px"></div>
      </div>
    </div>
    <div class="bar">Nachos: <small>corn chips n stuff</small></div>
    <ul class="items price-list">
      <li><span><b>Nachos guacamole:</b> corn chips, salsa, guacamole, sour cream &amp; cheese.</span><span class="amt">$7.00</span></li>
      <li><span><b>Nachos beef:</b> corn chips salsa, beef chilli, sour cream &amp; cheese.</span><span class="amt">$7.00</span></li>
      <li><span><b>Macho nachos:</b> all of the above.</span><span class="amt">$9.00</span></li>
      <li><span><b>Fries</b></span><span class="amt">$4.00</span></li>
    </ul>
    <h2 class="section-title" style="margin-top:18px">Belgian Waffles</h2>
    <div style="display:flex;align-items:center;gap:12px">
      <p class="tagline">(Not frozen)</p>
      <div class="art" role="img" aria-label="Sketch of a round Belgian waffle" style="width:110px;height:54px;border-radius:50%"></div>
      <div class="price">$9<sup>.50</sup></div>
    </div>
    <p class="blurb" style="margin-top:12px">House made waffles freshly made while you wait! Served with fresh strawberries, pure Canadian maple syrup, Belgian chocolate and fresh cream. Enough said.</p>
    <p class="fineprint">We source and use the best quality ingredients and serve it the freshest way possible. All menu items have been prepared with care and are cooked fresh while you wait. Please be patient as your food is being made.</p>
  </section>
</main>
</body>
</html>
```